An envelope for Housekeepers / The Velvet Lantern

Globally, 212 million people are employed in the hospitality industry. While many get commemorated for their work, there is one job that is often looked over.
Housekeepers hardly ever get told how great of a job they are doing.
Our company QuillbrookCo is seeking to empower housekeepers by allowing our guests to tip them through a cool envelope.
The plan :
- Create an envelope that has a message on it, which will incentivize our clientele to tip their housekeepers at check-out, and give housekeepers the credit they deserve for their hard work.
Example :
- "Humans do well by doing good" / "a thank you for your housekeeper"
What to do :
- Create an envelope based on the attached file. The white page titled "The Velvet Lantern" will be the front of the envelope (feel free to improve it but we really like the concept of it). The four blue pages will be the back pages of the envelope. Feel free to scour the web for quotes & embodying the same message of generosity.
We are really looking forward to seeing what kind of creative envelope you can conjure.
PS : remember that the goal with this envelope is to empower housekeepers & incentivize guests to tip them.
Target Market(s)
Travelers & housekeepers
Industry/Entity Type
Hospitality
Other font styles liked:
- Trebuchet, Times New Roman
Requirements
Must have
- Our project must have :
- - A white first page titled "The Velvet Lantern" is a must
- - You can improve it, but do not change the concept of it
- - Font : simple & easy to read
- - Color of back page : Teal
Nice to have
- Always keep in mind that this envelope is made to empower housekeepers.
Should not have
- Just keep it simple. Don't complicate things.

```html
<!DOCTYPE html>
<html lang="en">
<head>
<meta charset="utf-8">
<title>The Velvet Lantern – Housekeeper Envelope</title>
<link href="https://fonts.googleapis.com/css2?family=Didact+Gothic&family=Varela+Round&family=Allura&display=swap" rel="stylesheet">
<style>
  :root{
    --teal:#86c9e7;
    --white:#ffffff;
    --paper-shadow:rgba(0,0,0,0.18);
  }
  html,body{margin:0;padding:0;overflow:hidden;background:var(--white);}
  .canvas{position:relative;width:1200px;height:846px;overflow:hidden;background:var(--white);}

  .envelope{position:absolute;}
  .flap{position:absolute;display:block;overflow:visible;}
  .envelope-body{position:absolute;box-shadow:0 1px 4px var(--paper-shadow);}

  /* Front */
  .front .flap{left:154px;top:83px;}
  .front .envelope-body{left:154px;top:178px;width:413px;height:564px;background:var(--white);}
  .front-title{
    position:absolute;left:0;right:0;top:193px;margin:0;
    font-family:"Didact Gothic",sans-serif;font-weight:400;font-size:37px;line-height:40px;
    letter-spacing:0.42em;text-align:center;color:var(--teal);padding-left:0.42em;
  }
  .front-by{position:absolute;left:0;right:0;top:446px;text-align:center;
    font-family:"Didact Gothic",sans-serif;font-size:12px;color:var(--teal);letter-spacing:0.05em;}
  .brand-band{position:absolute;left:0;right:0;bottom:0;height:96px;background:var(--teal);}

  .brand{position:absolute;display:flex;align-items:center;gap:10px;}
  .brand-dot{width:40px;height:40px;border:2.5px solid var(--white);border-radius:50%;box-sizing:border-box;}
  .brand-name{font-family:"Didact Gothic",sans-serif;font-size:21px;line-height:19px;color:var(--white);margin:0;}
  .front .brand{left:120px;top:27px;}

  /* Back */
  .back .envelope-body{left:600px;top:178px;width:413px;height:564px;background:var(--teal);}
  .back .flap{left:600px;top:178px;}
  .quote{position:absolute;left:54px;top:190px;width:330px;margin:0;color:var(--white);font-family:"Varela Round",sans-serif;}
  .quote-lead{display:flex;align-items:flex-end;font-size:42px;line-height:42px;}
  .quote-rule{display:inline-block;height:3px;background:var(--white);}
  .quote-lead .quote-rule{width:136px;margin-left:8px;margin-bottom:3px;}
  .quote-middle{font-size:22px;line-height:26px;margin-top:6px;}
  .quote-end{display:flex;align-items:flex-end;font-size:42px;line-height:40px;}
  .quote-end .quote-rule{width:164px;margin-right:2px;margin-bottom:8px;}
  .quote-source{position:absolute;left:56px;top:320px;font-family:"Didact Gothic",sans-serif;font-size:11px;letter-spacing:0.28em;color:var(--white);}
  .thanks{position:absolute;left:0;right:0;top:398px;text-align:center;font-family:"Allura",cursive;font-size:25px;color:var(--white);}
  .back .brand{left:142px;top:475px;}
</style>
</head>
<body>
<main class="canvas">

  <section class="envelope front" aria-label="Envelope front">
    <svg class="flap" width="413" height="96" viewBox="0 0 413 96" aria-hidden="true">
      <polygon points="32,0 381,0 413,96 0,96" fill="var(--teal)"/>
      <circle cx="206" cy="65" r="31" fill="none" stroke="var(--white)" stroke-width="3.5"/>
    </svg>
    <div class="envelope-body">
      <h1 class="front-title">The<br>Velvet<br>Lantern</h1>
      <div class="front-by">BY</div>
      <div class="brand-band">
        <div class="brand">
          <span class="brand-dot"></span>
          <p class="brand-name">QUILLBROOK<br>CO</p>
        </div>
      </div>
    </div>
  </section>

  <section class="envelope back" aria-label="Envelope back">
    <div class="envelope-body">
      <blockquote class="quote">
        <div class="quote-lead">No One<span class="quote-rule"></span></div>
        <div class="quote-middle">has ever become poor by</div>
        <div class="quote-end"><span class="quote-rule"></span>Giving.</div>
      </blockquote>
      <div class="quote-source">MARA LINDEN</div>
      <p class="thanks">A thank you for your housekeeper</p>
      <div class="brand">
        <span class="brand-dot"></span>
        <p class="brand-name">QUILLBROOK<br>CO</p>
      </div>
    </div>
    <svg class="flap" width="413" height="94" viewBox="0 0 413 94" aria-hidden="true">
      <polygon points="0,0 413,0 382,92 32,92" fill="var(--white)" style="filter:drop-shadow(0 2px 2px rgba(0,0,0,0.25))"/>
      <circle cx="206" cy="46" r="31" fill="none" stroke="var(--teal)" stroke-width="3.5"/>
    </svg>
  </section>

</main>
</body>
</html>
```